Welding and farication business card

Business name Tbm Welding & Fabrication

I need a business card made for my welding and fabrication business that is bold and stands out. My business is both welding repairs on machinery and anything else you can imagine as well as fabricating new products. i have used this service before and was very happy with the out come of my design logo. i think the card should remain fairly simple and classy but also be bold. I think a black card would best be suited to the talk with my logo on it. i feel the back of the card should just have my logo and the front have my logo email, website and phone number and maybe incorporate a facebook and instagram simple if it can be made look good these arnt a necessity.
I have included both my logo and some business card ideas below

Target Market(s)

Farmers, heavy industry, earthmoving, trucking

Industry/Entity Type

Engineering

Contact Information for Business Card

0438517264
dale@tbmweldingandfabrication.com.au
www.tbmweldingandfabrication.com.au

Colors
33a6d7
0255a3

Requirements
Must have
• Dale Hutchins
my phone number 0438517264
my logo
Preferably a black card desgn
Nice to have
• List of what i do,
Sheds and carports
Ute trays
Stockyards
Trailers
Farm equipment
Stockcrates
Gateways and Entrances
Breakdowns
Maintenance
And lots more!

```html
<!DOCTYPE html>
<html lang="en">
<head>
<meta charset="utf-8">
<title>Tbm Welding &amp; Fabrication – Business Card</title>
<link rel="stylesheet" href="https://fonts.googleapis.com/css2?family=Oswald:wght@500&family=Krona+One&family=Roboto:wght@400&display=swap">
<style>
  :root {
    --backdrop: #2b2b2d;
    --card: #050505;
    --brand-blue: #0255a3;
    --spark-blue: #33a6d7;
    --text: #f4f4f4;
    --pattern-light: #1a1b1e;
    --pattern-dark: #070708;
  }
  html, body {
    margin: 0;
    width: 1200px;
    height: 1108px;
    overflow: hidden;
    background: var(--backdrop);
  }
  .canvas {
    position: relative;
    width: 1200px;
    height: 1108px;
  }
  .card {
    position: absolute;
    top: 124px;
    width: 520px;
    height: 860px;
    background: var(--card);
    border-radius: 26px;
    box-shadow: 0 18px 40px rgba(0,0,0,.55);
    overflow: hidden;
  }
  .card--front { left: 50px; }
  .card--back { left: 630px; }

  .brand-name {
    position: absolute;
    left: 40px;
    right: 40px;
    text-align: center;
    font-family: "Oswald", sans-serif;
    font-weight: 500;
    font-size: 58px;
    line-height: 1.05;
    text-transform: uppercase;
    color: var(--brand-blue);
    margin: 0;
  }
  .card--front .brand-name { top: 92px; }
  .card--back .brand-name { top: 150px; }

  .contact-icons {
    position: absolute;
    top: 296px;
    left: 0;
    right: 0;
    display: flex;
    justify-content: center;
    gap: 14px;
  }
  .contact-icons svg { width: 52px; height: 52px; display: block; }

  .phone {
    position: absolute;
    top: 368px;
    left: 0;
    right: 0;
    text-align: center;
    font-family: "Krona One", sans-serif;
    font-size: 34px;
    letter-spacing: 2px;
    color: var(--text);
    margin: 0;
  }
  .email, .website {
    position: absolute;
    left: 0;
    right: 0;
    text-align: center;
    font-family: "Roboto", sans-serif;
    font-size: 21px;
    color: var(--text);
    margin: 0;
  }
  .email { top: 428px; }
  .website { top: 460px; }
  .website .domain { color: var(--brand-blue); }

  .services {
    position: absolute;
    top: 526px;
    left: 56px;
    right: 30px;
    margin: 0;
    padding: 0;
    list-style: none;
    font-family: "Oswald", sans-serif;
    font-weight: 500;
    font-size: 31px;
    line-height: 1.42;
    text-transform: uppercase;
    color: var(--text);
  }
  .services .row { display: block; }
  .services .item { display: inline-block; margin-right: 24px; }
  .services .item.bullet::before {
    content: "";
    display: inline-block;
    width: 11px;
    height: 11px;
    border-radius: 50%;
    background: var(--brand-blue);
    margin-right: 12px;
    vertical-align: 0.5em;
  }

  .back-pattern {
    position: absolute;
    inset: 0;
    background:
      radial-gradient(ellipse at 70% 30%, var(--pattern-light), transparent 60%),
      radial-gradient(ellipse at 30% 75%, var(--pattern-light), transparent 55%),
      linear-gradient(160deg, #121315, var(--pattern-dark) 75%);
  }
</style>
</head>
<body>
<main class="canvas">

  <section class="card card--front" aria-label="Card front">
    <h1 class="brand-name">Tbm Welding &amp; Fabrication</h1>

    <div class="contact-icons">
      <svg viewBox="0 0 52 52" aria-label="Phone">
        <circle cx="26" cy="26" r="26" fill="var(--brand-blue)"/>
        <path d="M21 16c-3 2-4 5-3 10s4 9 8 11c2 1 4 0 5-1l-3-4-3 1c-2-2-3-5-3-8l3-1-1-5z" fill="#fff"/>
      </svg>
      <svg viewBox="0 0 52 52" aria-label="Email">
        <circle cx="26" cy="26" r="26" fill="var(--brand-blue)"/>
        <rect x="14" y="18" width="24" height="16" fill="#fff"/>
        <path d="M14 18l12 9 12-9M14 34l9-8M38 34l-9-8" stroke="var(--brand-blue)" stroke-width="1.6" fill="none"/>
      </svg>
      <svg viewBox="0 0 52 52" aria-label="Website">
        <circle cx="26" cy="26" r="26" fill="var(--brand-blue)"/>
        <circle cx="26" cy="26" r="12" fill="#fff"/>
        <path d="M20 19c3 1 5 3 4 6s-4 2-5 5M30 17c-1 3 1 5 4 5M29 30c2 1 3 3 2 5" stroke="var(--brand-blue)" stroke-width="2.4" fill="none"/>
      </svg>
    </div>

    <p class="phone">0438517264</p>
    <p class="email">dale@tbmweldingandfabrication.com.au</p>
    <p class="website">www.<span class="domain">tbmweldingandfabrication</span>.com.au</p>

    <ul class="services">
      <li class="row"><span class="item bullet">Sheds</span><span class="item bullet">Ute trays</span></li>
      <li class="row"><span class="item bullet">Cattle and sheep yards</span></li>
      <li class="row"><span class="item bullet">Trailers</span><span class="item bullet">Farm equipment</span></li>
      <li class="row"><span class="item bullet">Gateways and entrances</span></li>
      <li class="row"><span class="item">And lots more ...</span></li>
    </ul>
  </section>

  <section class="card card--back" aria-label="Card back">
    <div class="back-pattern" role="img" aria-label="Faint repeating pattern of welding torches and sparks in near-black tones covering the card"></div>
    <h2 class="brand-name">Tbm Welding &amp; Fabrication</h2>
  </section>

</main>
</body>
</html>
```